Marigold Shore Realty business card design

Looking for an upscale and clean business card design and updated logo. I sell to a very high-end south Florida real estate market.
Target Market(s)
High-end real estate in south Florida real estate market
Industry/Entity Type
Real Estate Agent
Contact Information for Business Card
Marigold Shore Realty, Inc
738 West Penrick Ave, Suite 400/500, Fort Lauderdale, FL 33315
Tim Harlow - Broker/Owner
954-327-8846 Direct
timshomes@quillmail.net
Website: StayPenrickAv.net
Font styles to use
Other font styles liked:
- Copperplate Gothic, Georgia, etc.
Requirements
Must have
- My photo, company name, my name and title, all info stated in Details above
Nice to have
- Luxury home design element, waterfront

```html
<!DOCTYPE html>
<html lang="en">
<head>
<meta charset="utf-8">
<title>Marigold Shore Realty — Business Card</title>
<link href="https://fonts.googleapis.com/css2?family=EB+Garamond:wght@400;500&display=swap" rel="stylesheet">
<style>
  :root {
    --navy: #15204a;
    --navy-deep: #0f1839;
    --gold: #f2cf1f;
    --gold-deep: #c9a30f;
    --white: #ffffff;
    --paper: #ffffff;
  }
  * { box-sizing: border-box; margin: 0; padding: 0; }
  html, body { width: 1200px; height: 1200px; overflow: hidden; background: var(--paper); }
  body { font-family: "EB Garamond", Georgia, serif; position: relative; }

  .card {
    position: absolute;
    top: 445px;
    width: 540px;
    height: 309px;
    background: radial-gradient(ellipse at 50% 40%, #1b2857 0%, var(--navy) 55%, var(--navy-deep) 100%);
    overflow: hidden;
  }
  .card--front { left: 40px; }
  .card--back { left: 620px; }

  /* Front */
  .front-mark {
    position: absolute;
    left: 50%;
    top: 52px;
    width: 110px;
    height: 110px;
    margin-left: -55px;
    border-radius: 50%;
    background: linear-gradient(160deg, var(--gold) 0%, var(--gold-deep) 100%);
  }
  .front-name {
    position: absolute;
    left: 0; right: 0;
    top: 226px;
    text-align: center;
    color: var(--gold);
    font-size: 34px;
    font-weight: 500;
    letter-spacing: 0.3px;
  }

  /* Back */
  .brand-mark {
    position: absolute;
    left: 40px; top: 22px;
    width: 42px; height: 42px;
    border-radius: 50%;
    background: linear-gradient(160deg, var(--gold) 0%, var(--gold-deep) 100%);
  }
  .brand-name {
    position: absolute;
    left: 98px; top: 30px;
    color: var(--gold);
    font-size: 22px;
    font-weight: 500;
  }
  .address {
    position: absolute;
    left: 48px; top: 94px;
    color: var(--white);
    font-size: 16px;
    line-height: 22px;
  }
  .contacts {
    position: absolute;
    left: 48px; top: 155px;
    list-style: none;
    color: var(--white);
    font-size: 16px;
  }
  .contacts li { display: flex; align-items: center; height: 29px; }
  .contacts svg { width: 19px; height: 19px; margin-right: 12px; flex: none; }

  .portrait {
    position: absolute;
    right: 0; top: 30px;
    width: 188px; height: 279px;
    background: linear-gradient(180deg, #2a3a78 0%, #2b46a0 45%, #1e3380 100%);
  }
  .nameplate {
    position: absolute;
    left: 303px; top: 234px;
  }
  .nameplate__name {
    display: inline-block;
    background: var(--white);
    color: var(--navy);
    font-size: 20px;
    line-height: 22px;
    padding: 0 4px;
  }
  .nameplate__title {
    display: block;
    width: max-content;
    background: var(--white);
    color: var(--navy);
    font-size: 9px;
    line-height: 12px;
    padding: 0 5px;
    margin-top: 1px;
  }
  .stripes { position: absolute; left: 0; top: 284px; width: 353px; }
  .stripe { height: 3px; background: linear-gradient(90deg, var(--gold-deep), var(--gold)); margin-bottom: 3px; }
</style>
</head>
<body>

<section class="card card--front" aria-label="Card front">
  <div class="front-mark"></div>
  <h1 class="front-name">Marigold Shore Realty, Inc.</h1>
</section>

<section class="card card--back" aria-label="Card back">
  <div class="brand-mark"></div>
  <h2 class="brand-name">Marigold Shore Realty, Inc</h2>

  <p class="address">738 West Penrick Ave,<br>Suite 400/500, Fort Lauderdale, FL 33315</p>

  <ul class="contacts">
    <li>
      <svg viewBox="0 0 20 20"><circle cx="10" cy="10" r="10" fill="#fff"/><path d="M6.5 5c.6-.4 1.2-.3 1.5.2l1 1.7c.3.5.1 1-.3 1.3l-.6.4c.5 1.2 1.4 2.2 2.6 2.8l.5-.6c.4-.4.9-.5 1.3-.2l1.7 1c.5.3.6.9.2 1.5-.6.9-1.6 1.3-2.7.9C9 13.2 7 11.2 6.1 8.4c-.4-1.2 0-2.6.4-3.4z" fill="#15204a"/></svg>
      954-327-8846
    </li>
    <li>
      <svg viewBox="0 0 20 20"><circle cx="10" cy="10" r="10" fill="#fff"/><rect x="5.5" y="6.5" width="9" height="7" rx="1" fill="#15204a"/><path d="M5.8 7l4.2 3.3L14.2 7" stroke="#fff" stroke-width="0.9" fill="none"/></svg>
      timshomes@quillmail.net
    </li>
    <li>
      <svg viewBox="0 0 20 20"><circle cx="10" cy="10" r="10" fill="#fff"/><g fill="none" stroke="#15204a" stroke-width="1"><circle cx="10" cy="10" r="4.6"/><ellipse cx="10" cy="10" rx="2" ry="4.6"/><path d="M5.4 10h9.2M6 7.8h8M6 12.2h8"/></g></svg>
      StayPenrickAv.net
    </li>
  </ul>

  <div class="portrait" role="img" aria-label="Portrait photo of Tim Harlow in a blue blazer"></div>

  <div class="nameplate">
    <span class="nameplate__name">Tim Harlow</span>
    <span class="nameplate__title">Broker/Owner</span>
  </div>

  <div class="stripes"><div class="stripe"></div><div class="stripe"></div></div>
</section>

</body>
</html>
```